Flowchart

I need a nice graphic that doesn't look like a stock word/ppt graphic to show the organization of our office. Example included. The idea to get across is that all of the units work together and feed into each other. I need this asap so will likely award tomorrow
Please use all text and if possible incorporate logo.
Design should be around 8.5 X 11 or smaller. Landscape vs. Protrait doesn't matter much.
A few more notes.
no larger than 81/2 by 11
Landscape preferred
Landscape preferred
Landscape

```html
<!DOCTYPE html>
<html lang="en">
<head>
<meta charset="utf-8">
<title>Biosciences Graduate Organization</title>
<link rel="stylesheet" href="https://fonts.googleapis.com/css2?family=Open+Sans:wght@400;600&display=swap">
<style>
  :root {
    --page: #e4e4e4;
    --panel: #dedede;
    --spine: #7b7b7b;
    --lobe-shadow: #bcbcbc;
    --frame-light: #f4f4f4;
    --frame-dark: #9a9a9a;
    --label: #ffffff;
    --ink: #1e1e1e;
  }
  * { box-sizing: border-box; margin: 0; padding: 0; }
  html, body { width: 1200px; height: 815px; overflow: hidden; }
  body {
    background: var(--page);
    font-family: "Open Sans", Arial, sans-serif;
    position: relative;
  }
  .frame {
    position: absolute;
    left: 30px; top: 30px;
    width: 1150px; height: 758px;
    background: var(--panel);
    border: 8px solid transparent;
    border-image: linear-gradient(90deg, var(--frame-dark), var(--frame-light) 20%, var(--frame-dark) 45%, var(--frame-light) 70%, var(--frame-dark)) 1;
  }
  .org-shapes { position: absolute; left: 0; top: 0; }
  .unit-label {
    position: absolute;
    color: var(--label);
    text-align: center;
    font-size: 21px;
    line-height: 1.4;
  }
  .unit-label.large { font-size: 24px; line-height: 1.4; }
  .unit-duties {
    position: absolute;
    left: 463px;
    color: var(--ink);
    font-size: 19.5px;
    line-height: 26px;
    list-style: none;
  }
  .unit-duties li {
    position: relative;
    padding-left: 16px;
    margin-bottom: 3px;
  }
  .unit-duties li::before {
    content: "";
    position: absolute;
    left: 0; top: 11px;
    width: 6px; height: 6px;
    border-radius: 50%;
    background: var(--ink);
  }
</style>
</head>
<body>
  <div class="frame"></div>

  <svg class="org-shapes" width="1200" height="815" viewBox="0 0 1200 815" aria-hidden="true">
    <!-- shadows -->
    <path d="M300 60 A128 118 0 0 1 300 296 Z" fill="var(--lobe-shadow)" transform="translate(14 0)"/>
    <circle cx="283" cy="410" r="118" fill="var(--lobe-shadow)"/>
    <path d="M300 528 A128 120 0 0 1 300 768 Z" fill="var(--lobe-shadow)" transform="translate(14 0)"/>
    <!-- spine -->
    <rect x="146" y="36" width="168" height="756" fill="var(--spine)"/>
    <!-- lobes -->
    <path d="M146 60 H300 A120 118 0 0 1 300 296 H146 Z" fill="var(--spine)"/>
    <circle cx="298" cy="410" r="118" fill="var(--spine)"/>
    <path d="M146 528 H300 A120 120 0 0 1 300 768 H146 Z" fill="var(--spine)"/>
  </svg>

  <div class="unit-label" style="left:180px; top:138px; width:220px; line-height:44px;">Biosciences<br>Home Programs</div>
  <div class="unit-label" style="left:190px; top:345px; width:230px;">Committee on<br>Graduate<br>Admissions &amp;<br>Policy (CGAP)</div>
  <div class="unit-label large" style="left:170px; top:590px; width:250px;">Office of<br>Graduate<br>Education (OGE)</div>

  <ul class="unit-duties" style="top:118px;">
    <li>Supports students with department or program<br>specific degree progress and graduation requirements</li>
    <li>Administers program-specific core curriculum</li>
    <li>Eight departments and Six interdisciplinary programs</li>
  </ul>

  <ul class="unit-duties" style="top:355px;">
    <li>Administrative oversight of Biosciences<br>admissions, curriculum and policies</li>
    <li>Forum for cross-program discussion and<br>collaboration</li>
  </ul>

  <ul class="unit-duties" style="top:546px;">
    <li>Promotes the academic, personal &amp; professional<br>development of all students through comprehensive<br>programs and services</li>
    <li>Advocates for the best possible training and empowerment<br>of all students</li>
    <li>Develops and administers Biosciences–wide,<br>interdisciplinary curriculum</li>
  </ul>
</body>
</html>
```